Business Card Design - ThriveMetric

Looking for creative, modern design, two sided for ThriveMetric that is consistent with color and feel of website www.thrivemetric.net.

Back of card will be used to promote products or have a quote revolving around decisions, change, leadership, innovation, creativity. Back should also have space to promote website, but optional to use the icon. Front of the card will need to use the icon and have standard place for name, job title, phone and email. We are not looking to put a mailing address or fax. Also want space to place a few words/phrase explaining what we do...such as individual growth and organizational development or tools, training, information...in addition, want the linkpage icon small on the front somewhere as we are also on linkpage.

Vector file uploaded of icon.

Target Market(s)

Professional coaching for individual growth and organizational development

Industry/Entity Type

Business

Requirements
Must have
• Icon...see attached.

```html
<!DOCTYPE html>
<html lang="en">
<head>
<meta charset="utf-8">
<title>ThriveMetric Business Card</title>
<link href="https://fonts.googleapis.com/css2?family=Tinos:wght@400;700&family=Arimo:wght@400;700&display=swap" rel="stylesheet">
<style>
  :root {
    --backdrop: #d9dadc;
    --card: #ffffff;
    --card-edge: #c9cacc;
    --brand-blue: #1a6fb5;
    --bar-blue: #2a9be0;
    --bar-deep: #1468b3;
    --navy: #2b3a7a;
    --ink: #333333;
    --quote-ink: #3a3a3a;
    --accent: #2a97d6;
    --mark-fill: #5bb5ea;
  }
  * { margin: 0; padding: 0; box-sizing: border-box; }
  html, body { width: 1200px; height: 404px; overflow: hidden; }
  body { background: var(--backdrop); position: relative; font-family: "Tinos", "Times New Roman", serif; }

  .card {
    position: absolute; top: 47px; width: 542px; height: 310px;
    background: var(--card); border: 1px solid var(--card-edge);
  }
  .card--front { left: 46px; }
  .card--back { left: 614px; }

  /* Front */
  .front__bar-left {
    position: absolute; left: 0; top: 18px; width: 6px; height: 122px;
    background: linear-gradient(var(--bar-blue), var(--bar-deep));
  }
  .front__bar-right {
    position: absolute; right: 0; top: 124px; width: 7px; height: 176px;
    background: linear-gradient(var(--bar-blue), var(--bar-deep));
  }
  .brand { position: absolute; left: 28px; top: 30px; display: flex; align-items: center; gap: 16px; }
  .brand__mark { width: 104px; height: 104px; border-radius: 50%; background: var(--mark-fill); }
  .brand__name { font-weight: 700; font-size: 25px; color: var(--brand-blue); letter-spacing: 0.3px; }

  .contact {
    position: absolute; right: 40px; top: 124px; text-align: right; color: var(--ink);
  }
  .contact__name { font-size: 19px; line-height: 22px; font-weight: 700; color: var(--navy); margin-bottom: 12px; }
  .contact__title { font-size: 15px; font-weight: 400; }
  .contact__line { font-size: 13.5px; line-height: 19px; height: 19px; display: flex; justify-content: flex-end; align-items: center; gap: 5px; }
  .contact__line svg { width: 10px; height: 10px; fill: var(--ink); }
  .contact__square { width: 9px; height: 9px; background: var(--brand-blue); }
  .tagline { position: absolute; right: 40px; top: 246px; text-align: right; font-size: 13.5px; line-height: 19px; color: var(--ink); }

  /* Back */
  .quotes { position: absolute; left: 28px; top: 22px; list-style: none; font-family: "Arimo", Arial, sans-serif; }
  .quote { position: relative; padding-left: 30px; height: 54px; }
  .quote__dot {
    position: absolute; left: 0; top: 4px; width: 20px; height: 20px; border-radius: 50%;
    background: radial-gradient(circle, #e8f5fd 35%, var(--mark-fill) 100%); border: 1px solid var(--accent);
  }
  .quote__text { font-size: 14px; color: var(--quote-ink); white-space: nowrap; }
  .quote__mark { font-family: "Tinos", serif; font-weight: 700; font-size: 24px; color: var(--ink); line-height: 0; position: relative; }
  .quote__mark--open { top: 4px; margin-right: 3px; }
  .quote__mark--close { top: 12px; margin-left: 1px; }
  .quote__author { font-size: 14px; font-weight: 700; color: var(--accent); margin-top: 3px; padding-left: 14px; }
  .quote__author span { color: var(--quote-ink); font-weight: 400; }
</style>
</head>
<body>
  <section class="card card--front" aria-label="Card front">
    <div class="front__bar-left"></div>
    <div class="front__bar-right"></div>
    <div class="brand">
      <div class="brand__mark"></div>
      <div class="brand__name">ThriveMetric</div>
    </div>
    <div class="contact">
      <p class="contact__name">Your Name, <span class="contact__title">Title</span></p>
      <p class="contact__line">
        <svg viewBox="0 0 10 10" aria-hidden="true"><circle cx="5" cy="5" r="4.6" fill="none" stroke="#333" stroke-width="1"/><path d="M3 2.4l1.1-.3.6 1.5-.7.5c.3.7.8 1.2 1.5 1.5l.5-.7 1.5.6-.3 1.1C5.3 6.9 3.1 4.7 3 2.4z"/></svg>
        123-456-789
      </p>
      <p class="contact__line">
        <svg viewBox="0 0 10 10" aria-hidden="true"><path d="M1 3h8v5H1z" fill="none" stroke="#333" stroke-width="1"/><path d="M1 3l4 3 4-3z"/></svg>
        hello@thrivemetric.net
      </p>
      <p class="contact__line">
        <svg viewBox="0 0 10 10" aria-hidden="true"><g fill="none" stroke="#333" stroke-width="0.9"><circle cx="5" cy="5" r="4.3"/><ellipse cx="5" cy="5" rx="1.8" ry="4.3"/><path d="M0.7 5h8.6M1.5 2.8h7M1.5 7.2h7"/></g></svg>
        www.thrivemetric.net
      </p>
      <p class="contact__line">
        <span class="contact__square"></span>
        /linkpage
      </p>
    </div>
    <p class="tagline">Supporting individual growth<br>and organizational development.</p>
  </section>

  <section class="card card--back" aria-label="Card back">
    <ul class="quotes">
      <li class="quote"><span class="quote__dot"></span>
        <p class="quote__text"><span class="quote__mark quote__mark--open">&ldquo;</span>Try not to become a man of success, but rather a man of value.<span class="quote__mark quote__mark--close">&rdquo;</span></p>
        <p class="quote__author"><span>- </span>Alden Marsh</p></li>
      <li class="quote"><span class="quote__dot"></span>
        <p class="quote__text"><span class="quote__mark quote__mark--open">&ldquo;</span>The only constant is change.<span class="quote__mark quote__mark--close">&rdquo;</span></p>
        <p class="quote__author"><span>- </span>Corin Vale</p></li>
      <li class="quote"><span class="quote__dot"></span>
        <p class="quote__text"><span class="quote__mark quote__mark--open">&ldquo;</span>We are what we repeatedly do. Excellence is not an act, it is a habit.<span class="quote__mark quote__mark--close">&rdquo;</span></p>
        <p class="quote__author"><span>- </span>Petra Lind</p></li>
      <li class="quote"><span class="quote__dot"></span>
        <p class="quote__text"><span class="quote__mark quote__mark--open">&ldquo;</span>Simplicity is the ultimate sophistication.<span class="quote__mark quote__mark--close">&rdquo;</span></p>
        <p class="quote__author"><span>- </span>Lorenzo Bellamy</p></li>
      <li class="quote"><span class="quote__dot"></span>
        <p class="quote__text"><span class="quote__mark quote__mark--open">&ldquo;</span>Life is not fair - get used to it.<span class="quote__mark quote__mark--close">&rdquo;</span></p>
        <p class="quote__author"><span>- </span>Wes Harlow</p></li>
    </ul>
  </section>
</body>
</html>
```